New to ArtHarbor? This Contest is for you!

Are you new to ArtHarbor and looking to enter your first contest? Look no further! We're launching this special contest to help you get started on building a design portfolio at ArtHarbor!

Requirements:
* Create a beautiful and eye-catching graphic design which includes the words "Spot me at ArtHarbor!"
* Upload your design to this contest AND share it on Chatterly
* You must upload your entry before 12:00am 1 April
* This must be your very FIRST entry on ArtHarbor to be eligible to receive a prize. If you've already entered other ArtHarbor contests you won't be eligible to win the prizes
* Your design must adhere to our quality standards to be eligible to receive a prize

Prizes:
* There are 150 x $5 participation payments ($750) available to be awarded to high-quality designs
* First prize for the best design is $150
* Second prize is $100

Requirements
Must have
• Your design must contain the words "Spot me at ArtHarbor".
• This must be your first entry on ArtHarbor to be eligible for the prizes.
• Your design must adhere to our quality standards.
Should not have
• No stock images or overused concepts.

```html
<!DOCTYPE html>
<html lang="en">
<head>
<meta charset="utf-8">
<title>Rafiq Anwar – Spot me at ArtHarbor</title>
<link rel="stylesheet" href="https://fonts.googleapis.com/css2?family=Baloo+2:wght@800&family=Noto+Naskh+Arabic:wght@400&display=swap">
<style>
  :root {
    --red: #d63a28;
    --green: #148043;
    --yellow: #f3e823;
    --indigo: #4a4d9e;
    --gap: #ffffff;
    --ink: #231f20;
    --black: #000000;
    --title-yellow: #f2e62a;
    --title-blue: #4557a4;
    --avatar-tone: #f4d69c;
  }
  html, body {
    margin: 0;
    padding: 0;
    overflow: hidden;
    background: var(--gap);
  }
  .poster {
    display: block;
    width: 1200px;
    height: 1000px;
  }
  .quadrant--red { fill: var(--red); }
  .quadrant--green { fill: var(--green); }
  .quadrant--yellow { fill: var(--yellow); }
  .quadrant--indigo { fill: var(--indigo); }
  .greeting {
    font-family: "Baloo 2", "Arial Rounded MT Bold", sans-serif;
    font-weight: 800;
    font-size: 66px;
  }
  .greeting--english { fill: var(--title-yellow); }
  .greeting--german { fill: var(--ink); }
  .greeting--malay { fill: var(--title-blue); }
  .greeting--arabic {
    font-family: "Noto Naskh Arabic", serif;
    font-weight: 400;
    font-size: 92px;
    fill: #ffffff;
  }
  .avatar-area { fill: var(--avatar-tone); }
  .name-arc {
    font-family: "Baloo 2", "Arial Black", sans-serif;
    font-weight: 800;
    font-size: 84px;
    letter-spacing: 6px;
    fill: var(--black);
  }
  .entry-number {
    font-family: "Baloo 2", "Arial Black", sans-serif;
    font-weight: 800;
    font-size: 112px;
    fill: var(--black);
  }
  .call-to-action {
    font-family: "Baloo 2", "Arial Rounded MT Bold", sans-serif;
    font-weight: 800;
    font-size: 60px;
    fill: var(--ink);
  }
</style>
</head>
<body>
<svg class="poster" viewBox="0 0 1200 1000" xmlns="http://www.w3.org/2000/svg">
  <defs>
    <path id="name-curve" d="M 295 612 Q 635 800 975 612"/>
  </defs>

  <g class="backdrop">
    <rect class="quadrant--red" x="0" y="0" width="617" height="519"/>
    <rect class="quadrant--green" x="627" y="0" width="573" height="519"/>
    <rect class="quadrant--yellow" x="0" y="527" width="617" height="473"/>
    <rect class="quadrant--indigo" x="627" y="527" width="573" height="473"/>
  </g>

  <g class="greetings">
    <text class="greeting greeting--english" x="592" y="220" text-anchor="end">My name is</text>
    <text class="greeting greeting--german" x="655" y="222">ich heiße</text>
    <text class="greeting greeting--malay" x="78" y="340">Nama Saya</text>
    <text class="greeting greeting--arabic" x="990" y="342" text-anchor="middle">اسمي</text>
  </g>

  <rect class="avatar-area" role="img" aria-label="Cartoon avatar of the designer"
        x="480" y="268" width="300" height="380" rx="28"/>

  <text class="name-arc"><textPath href="#name-curve" startOffset="50%" text-anchor="middle">RAFIQ ANWAR</textPath></text>

  <text class="entry-number" x="622" y="828" text-anchor="middle">10</text>

  <text class="call-to-action" x="645" y="920" text-anchor="middle">Spot me at ArtHarbor</text>
</svg>
</body>
</html>
```